BRIGHT COLORFUL + 55 FAMILY HISTORY BROCHURE 11 x 17 bifold

11 x 17 Bifold Flyer I have given you the Layout I just need you to make it Pretty

YOU DO NOT NEED TO FOLLOW MY LAYOUT, You can but dont have too

Target Market(s)

55 year old consumers, who could choose our service of Hereditary Cancer Screening

Industry/Entity Type

Health And Wellness

Requirements
Must have
• Must be appealing to Grand Parents, must make them want to test , show lots of pictures of grand children, YOU DO NOT NEED TO FOLLOW MY LAYOUT , You can but dont have too
Nice to have
• use our colors of our logo , YOU DO NOT NEED TO FOLLOW MY LAYOUT , You can but dont have too
Should not have
• YOU DO NOT NEED TO FOLLOW MY LAYOUT, You can but dont have too

```html
<!DOCTYPE html>
<html lang="en">
<head>
<meta charset="utf-8">
<title>Hereditary Cancer Screening – Bifold Brochure</title>
<link href="https://fonts.googleapis.com/css2?family=Libre+Baskerville:wght@400;700&family=Comic+Neue:wght@700&display=swap" rel="stylesheet">
<style>
  :root {
    --navy: #2b3565;
    --green: #8dc63f;
    --paper: #f7f8fa;
    --backdrop: #dfe2e6;
    --white: #ffffff;
    --photo-warm: linear-gradient(135deg, #e9dccd 0%, #c9b7a6 45%, #8e9bb8 100%);
    --photo-garden: linear-gradient(135deg, #7c9a52 0%, #d8a7b8 50%, #c6cbd6 100%);
    --photo-bright: linear-gradient(135deg, #eef0f2 0%, #d7c2b0 45%, #4f69a8 100%);
  }
  * { box-sizing: border-box; margin: 0; padding: 0; }
  html, body { width: 1200px; height: 789px; overflow: hidden; background: var(--backdrop); }
  body { font-family: "Libre Baskerville", Georgia, serif; }
  .spread { position: absolute; left: 25px; top: 22px; width: 1150px; height: 745px; display: flex; box-shadow: 0 6px 20px rgba(0,0,0,.18); }
  .page { position: relative; width: 575px; height: 745px; background: var(--paper); overflow: hidden; }
  .page--back { border-right: 1px solid #d4d7dc; }
  .photo { position: absolute; }
  .photo--warm { background: var(--photo-warm); }
  .photo--garden { background: var(--photo-garden); }
  .photo--bright { background: var(--photo-bright); }

  /* back page */
  .hook { position: absolute; left: 30px; top: 40px; width: 515px; height: 64px; background: var(--navy); border-left: 10px solid var(--green); padding: 10px 16px; color: var(--white); font-weight: 700; font-size: 15px; line-height: 1.35; }
  .hook .accent { color: var(--green); }
  .decision { position: absolute; left: 30px; top: 345px; width: 215px; height: 148px; background: var(--green); color: var(--white); font-weight: 700; font-size: 14px; line-height: 1.35; text-align: center; padding: 16px 10px; }
  .belief { position: absolute; left: 30px; top: 493px; width: 515px; height: 125px; background: var(--navy); padding: 14px 20px; }
  .belief__title { color: var(--green); font-weight: 700; font-size: 16px; line-height: 1.3; margin-bottom: 10px; }
  .belief__body { color: var(--white); font-size: 9.5px; line-height: 1.45; }
  .brand { position: absolute; right: 30px; top: 634px; display: flex; align-items: center; gap: 8px; color: var(--navy); font-weight: 700; font-size: 14px; line-height: 1.1; }
  .brand__dot { width: 30px; height: 30px; border-radius: 50%; background: var(--green); }
  .web { position: absolute; font-weight: 700; font-size: 17px; color: var(--navy); }
  .web .accent { color: var(--green); }
  .web--back { left: 72px; top: 686px; }
  .corner-square { position: absolute; left: 30px; top: 683px; width: 28px; height: 28px; background: var(--green); }
  .rule { position: absolute; height: 4px; }
  .rule--navy { background: var(--navy); }
  .rule--green { background: var(--green); }

  /* front page */
  .masthead { position: absolute; left: 20px; top: 38px; width: 535px; height: 58px; background: var(--green); border-bottom: 5px solid var(--navy); display: flex; align-items: center; justify-content: center; }
  .masthead__title { font-family: "Comic Neue", "Comic Sans MS", sans-serif; font-weight: 700; font-size: 31px; color: var(--navy); letter-spacing: .5px; }
  .tagline { position: absolute; left: 0; right: 0; top: 108px; text-align: center; color: var(--green); font-weight: 700; font-size: 20px; }
  .tagline .mark { color: var(--navy); }
  .navy-block { position: absolute; left: 470px; top: 330px; width: 85px; height: 90px; background: var(--navy); }
  .question { position: absolute; left: 20px; top: 420px; width: 150px; height: 92px; background: var(--green); border: 4px solid var(--navy); color: var(--white); font-size: 10.5px; line-height: 1.35; padding: 10px 10px; }
  .gift { position: absolute; left: 240px; top: 518px; width: 315px; height: 58px; background: var(--green); color: var(--white); padding: 8px 12px; }
  .gift__title { font-weight: 700; font-size: 17px; }
  .gift__note { font-size: 9.5px; color: var(--navy); margin-top: 4px; }
  .web--front { left: 0; right: 0; top: 650px; text-align: center; }
</style>
</head>
<body>
<main class="spread">
  <section class="page page--back">
    <header class="hook">
      <span class="accent">DOES CANCER</span> Run in Your Family?<br>
      A Simple Swab Could SAVE a <span class="accent">Family Members LIFE</span>
    </header>
    <div class="photo photo--warm" style="left:30px;top:104px;width:515px;height:241px" role="img" aria-label="Grandfather laughing as a toddler kisses his cheek, grandmother beside them"></div>
    <div class="photo photo--garden" style="left:245px;top:300px;width:300px;height:193px" role="img" aria-label="Grandparents sitting outdoors with two smiling grandchildren"></div>
    <div class="decision">Your decision won't just affect you. It will also impact Your Family, since your test results may Forecast Their Cancer Risks, too.</div>
    <div class="belief">
      <h2 class="belief__title">We believe it is important to understand what can and cannot be learned with genetic testing.</h2>
      <p class="belief__body">Genetic mutations can increase risks for certain cancers, but this does not mean cancer will definitely develop. You should be prepared to receive positive or negative results. Most people receive Negative Results meaning no mutations associated with an increased risk for the Hereditary cancers.</p>
    </div>
    <div class="brand"><span class="brand__dot"></span><span>Kinward<br>Health<br>Group</span></div>
    <div class="corner-square"></div>
    <p class="web web--back">www.<span class="accent">familyRiskCheck</span>.com</p>
    <div class="rule rule--navy" style="left:30px;top:720px;width:330px"></div>
    <div class="rule rule--green" style="left:360px;top:720px;width:185px"></div>
  </section>

  <section class="page page--front">
    <header class="masthead"><h1 class="masthead__title">Hereditary Cancer Screening</h1></header>
    <p class="tagline"><span class="mark">“</span>The Test You Take For Them<span class="mark">”</span></p>
    <div class="photo photo--bright" style="left:20px;top:145px;width:535px;height:275px" role="img" aria-label="Laughing grandparents playing with two grandchildren at home"></div>
    <div class="navy-block"></div>
    <div class="photo photo--garden" style="left:170px;top:410px;width:385px;height:112px" role="img" aria-label="Three generations of a family smiling together on a sofa"></div>
    <div class="question">Will You give Your loved ones the Information to Beat Cancer in their lives ?</div>
    <div class="photo photo--warm" style="left:90px;top:512px;width:150px;height:100px" role="img" aria-label="Grandmother hugging her granddaughter"></div>
    <div class="gift">
      <p class="gift__title">Give Them the Gift of Knowledge</p>
      <p class="gift__note">knowing is better than not knowing. Knowledge is Power</p>
    </div>
    <p class="web web--front">www.<span class="accent">familyRiskCheck</span>.com</p>
    <div class="rule rule--green" style="left:20px;top:690px;width:535px"></div>
    <div class="rule rule--navy" style="left:20px;top:694px;width:320px"></div>
  </section>
</main>
</body>
</html>
```